New Business Card

We need to refresh our business cards. We designed these ourselves and we have no graphic design experience. We would like to find a new business card design that is professional and unique. We are an auto finance company. Feel free to play with the logo, but we would like to keep the eye very present on the card. Our corporate colors are green, grey, and white.
Green - RGB - 168,215,27; HEX - #AADD22
Grey - RGB - 196,196,196; HEX - #C4C4C4
Need to upload the vector file to finalize the project. The last logo was for a jpeg that didn't stretch well.
Industry/Entity Type
Financial Service
Contact Information for Business Card
Honestly don't know...I need your help!

```html
<!DOCTYPE html>
<html lang="en">
<head>
<meta charset="utf-8">
<title>Brightlane Capital – Business Card</title>
<link href="https://fonts.googleapis.com/css2?family=Open+Sans:wght@400;600&display=swap" rel="stylesheet">
<style>
  :root {
    --brand-green: #AADD22;
    --green-soft: #c2e85a;
    --brand-grey: #C4C4C4;
    --text-dark: #2b2b2b;
    --paper: #ffffff;
    --backdrop: #3b3e42;
  }
  * { margin: 0; padding: 0; box-sizing: border-box; }
  html, body {
    width: 1200px; height: 1200px; overflow: hidden;
    background: var(--backdrop);
    font-family: "Open Sans", Arial, sans-serif;
  }
  .stage { position: relative; width: 1200px; height: 1200px; }
  .card {
    position: absolute; left: 150px; width: 900px; height: 514px;
    overflow: hidden; box-shadow: 0 10px 30px rgba(0,0,0,.35);
  }
  .card-front { top: 60px; background: var(--brand-green); }
  .card-back { top: 620px; background: var(--paper); }

  .wordmark { display: flex; align-items: center; gap: 14px; font-weight: 400; }
  .wordmark-dot { border-radius: 50%; flex: none; }
  .wordmark-text { display: flex; flex-direction: column; line-height: 1; }
  .wordmark-name { letter-spacing: .5px; }
  .wordmark-sub { letter-spacing: 12px; margin-top: 6px; }

  .card-front .wordmark {
    position: absolute; left: 50%; top: 50%; transform: translate(-50%, -50%);
    color: var(--paper);
  }
  .card-front .wordmark-dot { width: 70px; height: 70px; background: var(--paper); }
  .card-front .wordmark-name { font-size: 46px; }
  .card-front .wordmark-sub { font-size: 14px; }

  .card-back .wordmark {
    position: absolute; right: 60px; top: 48px; color: var(--brand-green);
  }
  .card-back .wordmark-dot { width: 54px; height: 54px; background: var(--brand-green); }
  .card-back .wordmark-name { font-size: 36px; }
  .card-back .wordmark-sub { font-size: 11px; letter-spacing: 10px; }

  .wave { position: absolute; left: 0; bottom: 0; width: 900px; height: 514px; }

  .holder { position: absolute; left: 70px; top: 150px; }
  .holder-name { font-size: 38px; font-weight: 600; letter-spacing: .5px; line-height: 1; }
  .holder-first { color: var(--brand-green); }
  .holder-last { color: var(--brand-grey); }
  .holder-role { font-size: 24px; color: var(--green-soft); margin-top: 4px; }

  .contact-list { position: absolute; left: 70px; top: 250px; list-style: none; }
  .contact-item {
    display: flex; align-items: center; gap: 16px;
    height: 50px; font-size: 16px; color: var(--text-dark); line-height: 1.25;
  }
  .contact-icon {
    width: 38px; height: 38px; border: 2px solid var(--brand-green); border-radius: 50%;
    display: flex; align-items: center; justify-content: center; flex: none;
  }
  .contact-icon svg { width: 20px; height: 20px; }
</style>
</head>
<body>
<main class="stage">

  <section class="card card-front" aria-label="Card front">
    <div class="wordmark">
      <span class="wordmark-dot"></span>
      <span class="wordmark-text">
        <span class="wordmark-name">Brightlane</span>
        <span class="wordmark-sub">CAPITAL</span>
      </span>
    </div>
  </section>

  <section class="card card-back" aria-label="Card back">
    <svg class="wave" viewBox="0 0 900 514" preserveAspectRatio="none" aria-hidden="true">
      <path d="M0 470 C 220 400, 420 370, 620 330 C 740 300, 820 250, 900 230 L900 514 L0 514 Z" fill="var(--green-soft)"/>
      <path d="M0 514 L0 500 C 260 440, 470 400, 640 340 C 760 290, 820 220, 900 170 L900 514 Z" fill="var(--brand-green)"/>
    </svg>

    <div class="wordmark">
      <span class="wordmark-dot"></span>
      <span class="wordmark-text">
        <span class="wordmark-name">Brightlane</span>
        <span class="wordmark-sub">CAPITAL</span>
      </span>
    </div>

    <div class="holder">
      <h1 class="holder-name"><span class="holder-first">MARCUS</span><span class="holder-last">HALE</span></h1>
      <p class="holder-role">Auto Finance Company</p>
    </div>

    <ul class="contact-list">
      <li class="contact-item">
        <span class="contact-icon"><svg viewBox="0 0 20 20" fill="none" stroke="#AADD22" stroke-width="1.6"><circle cx="10" cy="10" r="8"/><ellipse cx="10" cy="10" rx="3.5" ry="8"/><path d="M2 10h16M3.5 5.5h13M3.5 14.5h13"/></svg></span>
        <span>www.brightlanecap.com</span>
      </li>
      <li class="contact-item">
        <span class="contact-icon"><svg viewBox="0 0 20 20"><path d="M10 1.5a6 6 0 0 0-6 6c0 4.5 6 11 6 11s6-6.5 6-11a6 6 0 0 0-6-6z" fill="#AADD22"/><circle cx="10" cy="7.5" r="2.2" fill="#fff"/></svg></span>
        <span>58/B, Harbor Crest Plaza,<br>Oakridge, California</span>
      </li>
      <li class="contact-item">
        <span class="contact-icon"><svg viewBox="0 0 20 20" fill="none" stroke="#AADD22" stroke-width="1.6"><rect x="2" y="4.5" width="16" height="11"/><path d="M2 4.5l8 6.5 8-6.5M2 15.5l6-5M18 15.5l-6-5"/></svg></span>
        <span>hello@brightlanecap.com</span>
      </li>
      <li class="contact-item">
        <span class="contact-icon"><svg viewBox="0 0 20 20"><path d="M5 2l3 4-2 2c1 2.5 3.5 5 6 6l2-2 4 3-2 3C9 18 2 11 2 4z" fill="#AADD22"/></svg></span>
        <span>+(415) 555 018 273</span>
      </li>
    </ul>
  </section>

</main>
</body>
</html>
```